Book Cover Design Project

NOTE. I need the design in four days of posting this!

This will be the cover of my first book, WALK THE HIGH LINE -
alchemy in the real business world. The book explains defines what Purpose and Meaning is, and how to use it in business. I have included the first chapter to provide a background.

I want the core colours to be black and white, and use the colours Violet, Cerulean Blue Extra Pale (powder blue), Cadmium Lemon (flouro yellow). I plan on using this design as the basis for future books in the WALK THE HIGH LINE series, where the yellow is carried through but the violet and blue colours changing.

This is a spiritual business book without using any spiritual language. It is strongly masculine and direct in its nature.

What I am looking for is something Remarkable that captures my reader immediately. My reader is a seeker. He/she is an entrepreneur perhaps looking to setup a new venture and looking for new and better ways of doing things, or he/she may be a small/medium business owner perhaps bored looking for more meaning in personal and business life), or the corporate person who is looking to get out and do something new. Age 35-50.
Updates

Hi I want to correct the paper size. It is "C Format" (trade paperbacks) are 135mm x 216mm (5.32" x 8.51").

Thks

Reason: A deadline has changed which means the completion of this book cover is less time-critical.

This is a business book that introduces new concepts, such as Purpose. Although it is based on spiritual principals  it is using normal business language when explaining what Purpose is, and how businesses can identify it and use it to be more successful.

If there is a border between a self-help and a business book, this book sits close to the border but markedly on the business side.

Hi I want to confirm the book size. The book size I require is the Australian C Format, which measures 153mm W x 234mm H. 

Sorry for any confusion

Reason: Hi I have extended the deadline as I want to be able to print prospective covers and see how they look like in a bookshop next to other covers.

Reason: To allow for final negotiations.

Industry/Entity Type

Business

```html
<!DOCTYPE html>
<html lang="en">
<head>
<meta charset="utf-8">
<title>Walk the High Line – Book Cover</title>
<link href="https://fonts.googleapis.com/css2?family=Oswald:wght@300;400&family=Open+Sans:ital,wght@1,700&display=swap" rel="stylesheet">
<style>
  :root {
    --page: #ffffff;
    --violet: #3a2f86;
    --cerulean: #2a9fd0;
    --powder: #9fd3e6;
    --lemon: #d6dc2a;
    --moss: #5f8f3c;
    --deep-blue: #1f6fa8;
    --ink: #ffffff;
    --band: rgba(70, 70, 70, 0.85);
    --shade: rgba(40, 40, 40, 0.55);
  }
  html, body {
    margin: 0;
    width: 1200px;
    height: 900px;
    overflow: hidden;
    background: var(--page);
  }
  .canvas {
    position: relative;
    width: 1200px;
    height: 900px;
  }
  .cover {
    position: absolute;
    left: 360px;
    top: 28px;
    width: 506px;
    height: 812px;
    overflow: hidden;
  }
  .cover-texture {
    position: absolute;
    inset: 0;
    background:
      radial-gradient(ellipse 60% 30% at 10% 0%, var(--violet) 0%, transparent 80%),
      radial-gradient(ellipse 40% 35% at 75% 55%, var(--lemon) 0%, transparent 75%),
      radial-gradient(ellipse 35% 30% at 30% 75%, var(--lemon) 0%, transparent 75%),
      radial-gradient(ellipse 50% 25% at 50% 40%, var(--powder) 0%, transparent 80%),
      radial-gradient(ellipse 40% 25% at 90% 90%, var(--deep-blue) 0%, transparent 80%),
      linear-gradient(180deg, var(--deep-blue) 0%, var(--cerulean) 25%, var(--moss) 65%, var(--cerulean) 100%);
  }
  .author-name {
    position: absolute;
    top: 48px;
    left: 0;
    right: 0;
    margin: 0;
    text-align: center;
    font-family: "Oswald", sans-serif;
    font-weight: 300;
    font-size: 38px;
    letter-spacing: 11px;
    color: var(--ink);
  }
  .book-title {
    position: absolute;
    top: 140px;
    left: 40px;
    right: 24px;
    margin: 0;
    font-family: "Oswald", sans-serif;
    font-weight: 300;
    font-size: 116px;
    line-height: 156px;
    color: var(--ink);
    text-shadow: 2px 2px 0 var(--shade), 4px 4px 6px var(--shade);
    white-space: nowrap;
  }
  .book-title span { display: block; }
  .subtitle-band {
    position: absolute;
    left: 4px;
    right: 4px;
    top: 610px;
    height: 24px;
    background: var(--band);
    border-top: 2px solid var(--ink);
    border-bottom: 1px solid rgba(255,255,255,0.6);
    display: flex;
    align-items: center;
  }
  .subtitle {
    margin: 0 0 0 46px;
    font-family: "Open Sans", sans-serif;
    font-style: italic;
    font-weight: 700;
    font-size: 14.5px;
    color: var(--ink);
    white-space: nowrap;
  }
</style>
</head>
<body>
  <div class="canvas">
    <section class="cover">
      <div class="cover-texture" role="img" aria-label="Weathered painted wall texture in violet, cerulean blue and lemon yellow"></div>
      <p class="author-name">AUTHOR NAME</p>
      <h1 class="book-title"><span>WALK</span><span>THE HIGH</span><span>LINE</span></h1>
      <div class="subtitle-band">
        <p class="subtitle">Purpose and Meaning is, and how to use it in business</p>
      </div>
    </section>
  </div>
</body>
</html>
```